Bookkeeping Service Needs Postcard Design for Naturopaths

Looking for a postcard design targeted to naturopaths in the Portland, Oregon metro area.
Below is the text for front and back:
FRONT: You care for your patients. Let me care for your books.
BACK: Hiring an outside bookkeeper saves you time and money.
• No more second-guessing what your CPA and the IRS expect
• No more hours lost to maintaining your books
• No more questions about your financial health
• Accurate, individualized services available
• FREE 1-hour initial consultation
Call: 503-555-0187
Visit: www.larchvaleledgers.example
My business info:
Larchvale Ledgers
P.O. Box 40537
Portland, OR 97291
Logo attached. I have .ai, .psd and .eps files available if needed.
Looking for a design that is warm and eye-catching.
I am looking for a designer I can work with again to design more targeted postcards.
Target Market(s)
Naturopaths
Industry/Entity Type
Alternative Medicine

```html
<!DOCTYPE html>
<html lang="en">
<head>
<meta charset="utf-8">
<title>Larchvale Ledgers Postcard</title>
<link rel="stylesheet" href="https://fonts.googleapis.com/css2?family=Dancing+Script:wght@600&family=Open+Sans:wght@400;600;700&display=swap">
<style>
  :root {
    --page: #eeeeee;
    --blue: #2473bd;
    --blue-light: #4a97da;
    --navy: #1d3b66;
    --pale: #e6f0f9;
    --white: #ffffff;
    --line: #c9d3dd;
    --photo-a: #f1efee;
    --photo-b: #cfd6e0;
    --photo-c: #7a8a5a;
  }
  * { box-sizing: border-box; margin: 0; padding: 0; }
  html, body { width: 893px; height: 1200px; overflow: hidden; }
  body { background: var(--page); font-family: "Open Sans", Arial, sans-serif; position: relative; }

  .card { position: absolute; left: 42px; width: 809px; background: var(--white); overflow: hidden; box-shadow: 0 2px 6px rgba(0,0,0,.18); }
  .card--front { top: 50px; height: 515px; }
  .card--back { top: 595px; height: 535px; }

  .brand { position: absolute; display: flex; align-items: center; gap: 12px; }
  .brand__mark { width: 50px; height: 50px; border-radius: 50%; border: 4px solid currentColor; flex: none; }
  .brand__name { font-family: "Open Sans", Arial, sans-serif; font-weight: 600; font-size: 28px; line-height: 1.05; }

  /* front */
  .front__band { position: absolute; left: 0; top: 0; width: 100%; height: 125px; background: linear-gradient(90deg, var(--blue), var(--blue-light)); }
  .front__band .brand { left: 22px; top: 30px; color: var(--white); }
  .front__tagline { position: absolute; right: 28px; top: 14px; width: 440px; color: var(--white); font-family: "Dancing Script", cursive; font-size: 33px; line-height: 1.2; }
  .front__photo { position: absolute; left: 0; top: 125px; width: 100%; height: 365px;
    background: linear-gradient(100deg, var(--photo-c) 0%, #b7b3c4 22%, var(--photo-a) 45%, var(--photo-b) 100%); }
  .card__strip { position: absolute; left: 0; bottom: 0; width: 100%; height: 25px; background: var(--blue); }

  /* back */
  .back__info { position: absolute; left: 0; top: 0; width: 400px; height: 100%; background: var(--pale); padding: 28px 22px 0 26px; color: var(--navy); }
  .back__info .brand { position: static; color: var(--blue); }
  .back__headline { margin-top: 34px; font-family: "Dancing Script", cursive; font-size: 28px; line-height: 1.2; color: var(--navy); }
  .back__points { list-style: none; margin-top: 22px; font-size: 14.5px; line-height: 1.75; }
  .back__points li::before { content: "• "; }
  .back__contact { margin-top: 40px; font-size: 15px; font-weight: 700; line-height: 1.8; }
  .back__accent { position: absolute; left: 470px; top: 40px; width: 100px; height: 100px; border-radius: 50%; background: var(--pale); }
  .back__stamp { position: absolute; right: 40px; top: 38px; width: 112px; height: 132px; border: 2px solid var(--line); }
  .back__address { position: absolute; left: 470px; top: 240px; width: 300px; }
  .back__address span { display: block; height: 46px; border-bottom: 2px solid var(--line); }
</style>
</head>
<body>
  <section class="card card--front">
    <header class="front__band">
      <div class="brand">
        <span class="brand__mark"></span>
        <span class="brand__name">Larchvale<br>Ledgers</span>
      </div>
      <p class="front__tagline">You care for your patients.<br>Let me care for your books.</p>
    </header>
    <div class="front__photo" role="img" aria-label="Photo of a hand working on a laptop beside an essential-oil bottle and fresh herbs and flowers"></div>
    <div class="card__strip"></div>
  </section>

  <section class="card card--back">
    <div class="back__info">
      <div class="brand">
        <span class="brand__mark"></span>
        <span class="brand__name">Larchvale<br>Ledgers</span>
      </div>
      <h2 class="back__headline">Hiring an outside bookkeeper<br>saves you time and money.</h2>
      <ul class="back__points">
        <li>No more second-guessing what your CPA and<br>&nbsp;&nbsp;the IRS expect</li>
        <li>No more hours lost to maintaining your books</li>
        <li>No more questions about your financial health</li>
        <li>Accurate, individualized services available</li>
        <li>FREE 1-hour initial consultation</li>
      </ul>
      <p class="back__contact">Call: 503-555-0187<br>Visit: www.larchvaleledgers.example</p>
    </div>
    <div class="back__accent"></div>
    <div class="back__stamp"></div>
    <div class="back__address"><span></span><span></span><span></span><span></span></div>
    <div class="card__strip"></div>
  </section>
</body>
</html>
```